elegant beautiful Hang tag for a novelty makeup towel

It's a black hand towel in the shape of a little black dress. it is called VELVET EVENING WRAP, it is a SECRET KEEPER MAKEUP TOWEL. (doesn't show our makeup stains) Made in USA

Target Market(s)

ALL Women , Makeup artists, novelty THIS WILL BE IN THE HALVERSTEAD STORES AND PEMBERCROFT STORES.

Industry/Entity Type

Makeup

Contact Information for Business Card

I actually need a hang tag for a homemade handmade towel. I have a logo that I want on the tag and know what we want to say on it, on back needs to say "The essential to every girl's wardrobe. So when the little black dress comes off, our VELVET EVENING WRAP is there to help you wash your day away. Include website www.velveteveningwrap.com OH INCLUDE TM (trademark sign next to logo please. Also, in small print on back from the makers of THE ORIGINAL SECRET KEEPER MAKEUP TOWEL. handmade in USA. also SECRET KEEPER MAKEUP TOWEL IN big font on front under logo sign with light colored pink lips after 'SECRET KEEPER" but have no idea about fonts, graphics, placement or design. Want it classy, elegant, girly! COLORS LIGHT BEIGER BACKGROUND WITH BLACK WRITING/ DESIGNS

Font styles to use
Serif
Decorative
Script

Colors
fff3d1

Requirements
Must have
• Black cream girly , also state in big writing that it's a " secret keeper makeup towel" with a tiny light pink lip between the show and makeup. Include www.velveteveningwrap.com Brightfold Goods, LLC
Nice to have
• Perhaps an outline of a little black dress. A black scroll edge of some sort around card. Classy

```html
<!DOCTYPE html>
<html lang="en">
<head>
<meta charset="utf-8">
<title>Velvet Evening Wrap – Business Card</title>
<link href="https://fonts.googleapis.com/css2?family=Montserrat:wght@300;400;500;600&family=Shadows+Into+Light+Two&display=swap" rel="stylesheet">
<style>
  :root {
    --stage: #e9e9ea;
    --card-cream: #fff3d1;
    --card-cream-deep: #f3e3b8;
    --ink: #151110;
    --ink-soft: #3a322d;
    --accent-pink: #d77688;
    --rule: #1c1614;
  }
  * { box-sizing: border-box; margin: 0; padding: 0; }
  html, body {
    width: 1200px; height: 925px; overflow: hidden;
    background: var(--stage);
    font-family: "Montserrat", sans-serif;
  }
  .canvas { position: relative; width: 1200px; height: 925px; }

  .card {
    position: absolute; top: 91px;
    width: 423px; height: 739px;
    border-radius: 26px; overflow: hidden;
    box-shadow: 0 6px 14px rgba(0,0,0,0.22);
    color: var(--ink);
  }
  .card--front { left: 160px; }
  .card--back { left: 620px; }

  .card__photo {
    position: absolute; inset: 0;
    background:
      radial-gradient(ellipse at 35% 35%, #fff8e4 0%, transparent 60%),
      linear-gradient(170deg, var(--card-cream) 0%, var(--card-cream-deep) 100%);
  }

  .tm { font-family: "Montserrat", sans-serif; font-size: 0.4em; vertical-align: super; letter-spacing: 0; margin-left: 2px; }

  /* Front */
  .brand-mark {
    position: absolute; top: 140px; left: 0; right: 0;
    display: flex; align-items: center; justify-content: center; gap: 12px;
    font-weight: 500; font-size: 21px; letter-spacing: 2px;
  }
  .brand-mark__dot { width: 14px; height: 14px; border-radius: 50%; background: var(--ink); }

  .person { position: absolute; top: 468px; left: 0; right: 0; text-align: center; }
  .person__name { font-weight: 600; font-size: 27px; letter-spacing: 0.5px; line-height: 34px; }
  .person__role { font-weight: 400; font-size: 16.5px; color: var(--ink-soft); letter-spacing: 0.5px; }

  .rule {
    position: absolute; left: 88px; width: 248px; height: 2px;
    background: linear-gradient(90deg, transparent, var(--rule) 20%, var(--rule) 80%, transparent);
  }
  .rule--top { top: 517px; }
  .rule--bottom { top: 695px; }

  .contact { position: absolute; left: 0; right: 0; text-align: center; color: var(--ink); font-weight: 400; font-style: normal; }
  .contact--address { top: 530px; font-size: 17.5px; line-height: 23px; letter-spacing: 0.6px; }
  .contact__icons { position: absolute; top: 588px; left: 0; right: 0; display: flex; justify-content: center; gap: 6px; }
  .contact__icons svg { width: 14px; height: 14px; }
  .contact--lines { top: 613px; font-size: 17.5px; line-height: 23px; letter-spacing: 0.5px; }

  /* Back */
  .wordmark {
    position: absolute; left: 202px; top: 369px;
    transform: translate(-50%, -50%) rotate(-90deg);
    white-space: nowrap;
    font-family: "Shadows Into Light Two", cursive;
    font-weight: 400;
    font-size: 44px; letter-spacing: 4px; color: var(--ink);
    line-height: 1;
  }
  .tagline {
    position: absolute; left: 241px; top: 374px;
    transform: translate(-50%, -50%) rotate(-90deg);
    white-space: nowrap;
    font-weight: 400; font-size: 16px; letter-spacing: 0.8px;
    color: var(--accent-pink);
  }
  .vrule { position: absolute; left: 240px; width: 1.5px; background: var(--rule); }
  .vrule--upper { top: 89px; height: 123px; }
  .vrule--lower { top: 519px; height: 140px; }

  .origin {
    position: absolute; left: 0; right: 0; top: 680px;
    text-align: center; font-size: 11px; letter-spacing: 1px; line-height: 16px;
    color: var(--ink-soft);
  }
</style>
</head>
<body>
<main class="canvas">

  <section class="card card--front">
    <div class="card__photo" role="img" aria-label="Softly lit photograph of a black hand towel hanging on a bathroom towel bar"></div>

    <div class="brand-mark">
      <span class="brand-mark__dot"></span>
      <span>VELVET EVENING WRAP<span class="tm">TM</span></span>
    </div>

    <div class="person">
      <p class="person__name">Marla Quentin</p>
      <p class="person__role">Director</p>
    </div>

    <div class="rule rule--top"></div>

    <address class="contact contact--address">
      48 Foundry Lane<br>
      Millbrook, NY 12545
    </address>

    <div class="contact__icons" aria-hidden="true">
      <svg viewBox="0 0 16 16"><path d="M4 1.5l2.5 3-1.5 1.5c.8 2 2.3 3.5 4.5 4.5l1.5-1.5 3 2.5-1.5 2.5C7 13.5 2.5 9 1.5 3z" fill="none" stroke="var(--accent-pink)" stroke-width="1.4" stroke-linejoin="round"/></svg>
      <svg viewBox="0 0 16 16"><rect x="1.5" y="3.5" width="13" height="9" fill="none" stroke="var(--accent-pink)" stroke-width="1.4"/><path d="M1.5 3.5L8 9l6.5-5.5" fill="none" stroke="var(--accent-pink)" stroke-width="1.4"/></svg>
      <svg viewBox="0 0 16 16"><circle cx="8" cy="8" r="6.5" fill="none" stroke="var(--accent-pink)" stroke-width="1.3"/><ellipse cx="8" cy="8" rx="3" ry="6.5" fill="none" stroke="var(--accent-pink)" stroke-width="1.1"/><path d="M1.5 8h13M2.5 5h11M2.5 11h11" stroke="var(--accent-pink)" stroke-width="1"/></svg>
    </div>

    <p class="contact contact--lines">
      +330 5812-0394<br>
      info@velveteveningwrap.com<br>
      www.velveteveningwrap.com
    </p>

    <div class="rule rule--bottom"></div>
  </section>

  <section class="card card--back">
    <div class="card__photo" role="img" aria-label="Softly lit photograph of a towel draped over a towel bar in a bathroom"></div>

    <h1 class="wordmark">VELVET EVENING WRAP<span class="tm">TM</span></h1>
    <div class="vrule vrule--upper"></div>
    <p class="tagline">SECRET KEEPER MAKEUP TOWEL</p>
    <div class="vrule vrule--lower"></div>

    <p class="origin">The essential to every girl's wardrobe<br>HANDMADE IN USA</p>
  </section>

</main>
</body>
</html>
```